Landing page

I have a landing page script which has no design element whatsoever.
I need someone creative to take the script and make a design, including providing the HTML script once finished.
The landing page will include a video sales letter, some testimonials, 2 buttons (one which will show a pop-up with 3 confirmation checkboxes and another button which when pressed will open an embedded calendly window or pop-up.
Most importantly, the landing page must be designed with best conversion practises in mind.
The attached script is a draft, but the final copy it will be very similar in terms of length and content.
Branding package should be as per our website https://brightlanecargo.com
Target Market(s)
e-Commerce store owners and dropshippers
Coding
Coded - Design and coding required
Number of Pages Required
1 page
Look and feel
Each slider illustrates characteristics of the customer's brand and the style your logo design should communicate.

```html
<!DOCTYPE html>
<html lang="en">
<head>
<meta charset="utf-8">
<title>Bright Lane Cargo – Landing</title>
<link rel="stylesheet" href="https://fonts.googleapis.com/css2?family=Poppins:ital,wght@0,400;0,500;0,600;0,700;1,300;1,400;1,500&family=Roboto:wght@500&display=swap">
<style>
  :root {
    --brand-red: #ec1c24;
    --brand-navy: #1f2a44;
    --text-dark: #3a3a3a;
    --text-soft: #e8606a;
    --nav-text: #2b2b2b;
    --bg: #ffffff;
  }
  * { box-sizing: border-box; margin: 0; padding: 0; }
  html, body {
    width: 1200px; height: 675px; overflow: hidden;
    background: var(--bg);
    font-family: "Poppins", sans-serif;
  }
  .page { position: relative; width: 1200px; height: 675px; }

  .site-header {
    position: absolute; inset: 0 0 auto 0; height: 76px;
    background: var(--bg);
    box-shadow: 0 6px 22px rgba(0,0,0,0.08);
  }
  .brand {
    position: absolute; left: 19px; top: 22px;
    display: flex; align-items: center; gap: 6px;
    font-family: "Poppins", sans-serif; font-weight: 700;
    font-size: 15px; letter-spacing: 0.5px; color: var(--brand-navy);
  }
  .brand-mark { width: 10px; height: 10px; background: var(--brand-red); }

  .main-nav a {
    position: absolute; top: 32px;
    font-size: 12px; font-weight: 600; letter-spacing: 1px;
    color: var(--nav-text); text-decoration: none; text-transform: uppercase;
    white-space: nowrap;
  }
  .main-nav a.is-active { color: var(--brand-red); }
  .main-nav .caret { display: inline-block; width: 10px; height: 8px; margin-left: 6px; vertical-align: middle; }
  .nav-underline {
    position: absolute; left: 247px; top: 67px; width: 69px; height: 2px;
    background: var(--brand-red);
  }
  .btn {
    position: absolute; top: 24px; height: 33px;
    display: flex; align-items: center; justify-content: center;
    background: var(--brand-red); color: #fff;
    font-family: "Roboto", sans-serif; font-weight: 500; font-size: 12px;
    text-decoration: none; text-transform: uppercase; letter-spacing: 0.2px;
  }
  .btn-contact { left: 911px; width: 108px; }
  .btn-app { left: 1044px; width: 136px; }

  .hero-copy { position: absolute; left: 82px; top: 184px; }
  .hero-title {
    font-size: 48px; font-weight: 700; line-height: 53px;
    letter-spacing: -1px; color: var(--brand-red);
  }
  .hero-lead {
    margin-top: 26px; margin-left: 3px;
    font-size: 19px; font-weight: 600; color: var(--text-dark); letter-spacing: -0.3px;
  }
  .claims { list-style: none; margin-top: 22px; margin-left: 3px; }
  .claims li {
    font-size: 19px; font-style: italic; font-weight: 500;
    line-height: 22.5px; color: var(--text-dark);
  }
  .hero-aside {
    margin-top: 18px;
    font-size: 31px; font-style: italic; font-weight: 400; color: var(--text-soft);
  }

  .hero-visual {
    position: absolute; left: 572px; top: 169px; width: 609px; height: 412px;
    background: radial-gradient(circle at 50% 50%, #e8202a 0%, #ec2a33 44%, #f7c6cb 58%, rgba(255,255,255,0) 74%);
  }
</style>
</head>
<body>
<div class="page">
  <header class="site-header">
    <div class="brand"><span class="brand-mark"></span>BRIGHT LANE CARGO</div>
    <nav class="main-nav">
      <a href="https://brightlanecargo.com" class="is-active" style="left:263px">Home</a>
      <a href="#" style="left:336px">About Us<svg class="caret" viewBox="0 0 10 8"><path d="M1 2l4 4 4-4" fill="none" stroke="#2b2b2b" stroke-width="2"/></svg></a>
      <a href="#" style="left:451px">Service<svg class="caret" viewBox="0 0 10 8"><path d="M1 2l4 4 4-4" fill="none" stroke="#2b2b2b" stroke-width="2"/></svg></a>
      <a href="#" style="left:557px">FAQs</a>
      <a href="#" style="left:625px">Pricing</a>
      <a href="#" style="left:717px">Marketplace</a>
      <a href="#" style="left:846px">Blogs</a>
    </nav>
    <span class="nav-underline"></span>
    <a href="#" class="btn btn-contact">Contact Us</a>
    <a href="#" class="btn btn-app">Ecommerce App</a>
  </header>

  <section class="hero-copy">
    <h1 class="hero-title">How is this different<br>from anything else<br>I’ve seen?</h1>
    <p class="hero-lead">Are you tired of hearing the same old</p>
    <ul class="claims">
      <li>Cheaper than Marketvale</li>
      <li>Best dropshipping agent in China</li>
      <li>The most professional service</li>
      <li>Fastest worldwide shipping</li>
    </ul>
    <p class="hero-aside">Yada yada yada</p>
  </section>

  <div class="hero-visual" role="img" aria-label="Illustration of a red globe with warehouse workers, pallets of parcels and a forklift linked by dotted shipping routes"></div>
</div>
</body>
</html>
```